label design for coffee bean packaging

Logo will be provided. Label design for package of coffee beans for a micro roasted coffee company. Need to have space to write in origin, weight with check box for 1/4, 1/2, 1lb. Need to have check boxes for Light, Medium, Dark. Creative unique label design with boarders and fun, modern design. Company name is Cedar Brook Roasting Company. See attached logo. I have source files for logo if needed for design.
Industry/Entity Type
Coffee Shop
Font styles to use
Other font styles liked:
- Montez, kautiva cyrillic, uniform bold
Colors
f78f20
faa54b
f37122
fece3e
acd036
Requirements
Must have
- logo included in the design

```html
<!DOCTYPE html>
<html lang="en">
<head>
<meta charset="utf-8">
<title>Cedar Brook Roasting Company – Coffee Bean Label</title>
<link href="https://fonts.googleapis.com/css2?family=Source+Sans+3:wght@400;600&family=Courgette&display=swap" rel="stylesheet">
<style>
  :root {
    --roast-brown: #5a2d14;
    --leaf-grey: #a9a9a9;
    --leaf-light: #e6e6e6;
    --ink: #2b2b2b;
    --paper: #ffffff;
  }
  html, body {
    margin: 0;
    padding: 0;
    width: 1200px;
    height: 1200px;
    overflow: hidden;
    background: var(--paper);
  }
  .canvas {
    position: relative;
    width: 1200px;
    height: 1200px;
    font-family: "Source Sans 3", "Myriad Pro", sans-serif;
    color: var(--ink);
  }
  .label {
    position: absolute;
    left: 230px;
    top: 150px;
    width: 738px;
    height: 911px;
  }
  /* side panels with frame */
  .side-panel {
    position: absolute;
    top: 0;
    width: 120px;
    height: 911px;
  }
  .side-panel--left { left: 0; }
  .side-panel--right { right: 0; }
  .side-panel svg { display: block; }

  /* brand block */
  .brand {
    position: absolute;
    left: 169px;
    top: 80px;
    width: 400px;
    height: 428px;
    display: flex;
    flex-direction: column;
    align-items: center;
    justify-content: center;
    gap: 22px;
  }
  .brand__dot {
    width: 70px;
    height: 70px;
    border-radius: 50%;
    border: 4px solid var(--roast-brown);
  }
  .brand__name {
    margin: 0;
    font-family: "Source Sans 3", sans-serif;
    font-weight: 600;
    font-size: 46px;
    line-height: 1.1;
    color: var(--roast-brown);
    text-align: center;
  }

  .origin {
    position: absolute;
    left: 120px;
    width: 498px;
    top: 680px;
    margin: 0;
    text-align: center;
    font-family: "Courgette", cursive;
    font-weight: 400;
    font-size: 62px;
    line-height: 1;
    color: var(--roast-brown);
  }

  .roast-levels {
    position: absolute;
    left: 178px;
    top: 795px;
    display: flex;
    gap: 34px;
    font-size: 27px;
    color: var(--ink);
    letter-spacing: 0.2px;
  }
  .check {
    display: flex;
    align-items: center;
    gap: 4px;
  }
  .check__box {
    width: 18px;
    height: 18px;
    border: 1.5px solid var(--ink);
    box-sizing: border-box;
  }

  .date-roasted {
    position: absolute;
    left: 178px;
    top: 872px;
    margin: 0;
    font-size: 28px;
    line-height: 1;
    color: var(--ink);
  }

  .weight-band {
    position: absolute;
    left: 120px;
    top: 906px;
    width: 496px;
    height: 80px;
    background: var(--roast-brown);
    color: var(--paper);
    box-sizing: border-box;
    padding: 4px 0 0 58px;
  }
  .weight-band__title {
    margin: 0;
    font-size: 28px;
    line-height: 1.2;
  }
  .weight-options {
    display: flex;
    gap: 42px;
    font-size: 28px;
    line-height: 1.2;
    margin-top: 2px;
  }
  .weight-options .check__box {
    border: none;
    background: var(--paper);
    width: 20px;
    height: 20px;
    margin-right: 6px;
  }
  .band-rule {
    position: absolute;
    left: 120px;
    top: 990px;
    width: 496px;
    height: 3px;
    background: var(--roast-brown);
  }
  .website {
    position: absolute;
    left: 120px;
    width: 498px;
    top: 1012px;
    margin: 0;
    text-align: center;
    font-size: 20px;
    color: var(--roast-brown);
  }
</style>
</head>
<body>
<div class="canvas">
  <!-- panels positioned relative to the canvas for the lower elements -->
  <div class="label">
    <div class="side-panel side-panel--left">
      <svg width="120" height="911" viewBox="0 0 120 911">
        <defs>
          <linearGradient id="leafToneLeft" x1="0" y1="0" x2="1" y2="1">
            <stop offset="0" stop-color="var(--leaf-light)"/>
            <stop offset="0.5" stop-color="#cfcfcf"/>
            <stop offset="1" stop-color="var(--leaf-light)"/>
          </linearGradient>
        </defs>
        <rect x="30" y="30" width="90" height="851" fill="url(#leafToneLeft)" role="img" aria-label="Engraved coffee leaf illustration in soft grey"/>
        <rect x="0" y="0" width="120" height="22" fill="var(--roast-brown)"/>
        <rect x="0" y="889" width="120" height="22" fill="var(--roast-brown)"/>
        <rect x="0" y="0" width="22" height="911" fill="var(--roast-brown)"/>
        <rect x="30" y="30" width="4" height="851" fill="var(--roast-brown)"/>
        <rect x="30" y="30" width="90" height="4" fill="var(--roast-brown)"/>
        <rect x="30" y="877" width="90" height="4" fill="var(--roast-brown)"/>
      </svg>
    </div>
    <div class="side-panel side-panel--right">
      <svg width="120" height="911" viewBox="0 0 120 911">
        <defs>
          <linearGradient id="leafToneRight" x1="1" y1="0" x2="0" y2="1">
            <stop offset="0" stop-color="var(--leaf-light)"/>
            <stop offset="0.5" stop-color="#c8c8c8"/>
            <stop offset="1" stop-color="var(--leaf-light)"/>
          </linearGradient>
        </defs>
        <rect x="0" y="30" width="90" height="851" fill="url(#leafToneRight)" role="img" aria-label="Engraved coffee leaf illustration in soft grey"/>
        <rect x="0" y="0" width="120" height="22" fill="var(--roast-brown)"/>
        <rect x="0" y="889" width="120" height="22" fill="var(--roast-brown)"/>
        <rect x="98" y="0" width="22" height="911" fill="var(--roast-brown)"/>
        <rect x="86" y="30" width="4" height="851" fill="var(--roast-brown)"/>
        <rect x="0" y="30" width="90" height="4" fill="var(--roast-brown)"/>
        <rect x="0" y="877" width="90" height="4" fill="var(--roast-brown)"/>
      </svg>
    </div>

    <div class="brand">
      <div class="brand__dot"></div>
      <p class="brand__name">Cedar Brook<br>Roasting Company</p>
    </div>

    <h1 class="origin" style="top:530px;">Origin Name</h1>

    <div class="roast-levels" style="top:645px;">
      <span class="check"><span class="check__box"></span>LIGHT</span>
      <span class="check"><span class="check__box"></span>MEDIUM</span>
      <span class="check"><span class="check__box"></span>DARK</span>
    </div>

    <p class="date-roasted" style="top:724px;">Date Roasted:</p>

    <div class="weight-band" style="top:756px;">
      <p class="weight-band__title">Net. Wight:</p>
      <div class="weight-options">
        <span class="check"><span class="check__box"></span>1/4</span>
        <span class="check"><span class="check__box"></span>1/2</span>
        <span class="check"><span class="check__box"></span>1lb</span>
      </div>
    </div>
    <div class="band-rule" style="top:840px;"></div>

    <p class="website" style="top:862px;">www.cedarbrookroastingco.com</p>
  </div>
</div>
</body>
</html>
```